we need a business card as well as a logo that can be used for signs etc.
this is a very formal, classy , elegant function centre, as well as café. I am after a design that stands out and grabs people attentions. my colours theme is really warm ,colours like chocolate browns, and latte type colours with really deep red tones
not bright red, just warm tones. this is a place that very wealthy and maybe even celebs will come so I need it to be appealing.
Industry/Entity Type
Business
Contact Information for Business Card
Blue Fern
café and function centre @ hallam orchard.
wedding and function specialists,
Barrow parkway, dunmore,ph 0438157240

```html
<!DOCTYPE html>
<html lang="en">
<head>
<meta charset="utf-8">
<title>Blue Fern café and function centre – business card</title>
<link href="https://fonts.googleapis.com/css2?family=Open+Sans:wght@400;700&display=swap" rel="stylesheet">
<style>
  :root {
    --wood-light: #bd6a22;
    --wood-mid: #a9561a;
    --wood-dark: #7a3a10;
    --band-red: #9a4630;
    --band-shadow: #6b3418;
    --ornament-red: #a04a32;
    --ink-light: #ffffff;
  }
  html, body {
    margin: 0;
    padding: 0;
    width: 1200px;
    height: 666px;
    overflow: hidden;
    background: var(--wood-dark);
  }
  .card {
    position: relative;
    width: 1200px;
    height: 666px;
    overflow: hidden;
    font-family: "Open Sans", sans-serif;
    color: var(--ink-light);
    background:
      radial-gradient(ellipse 75% 80% at 60% 45%, var(--wood-light) 0%, var(--wood-mid) 55%, var(--wood-dark) 100%);
  }
  .side-band {
    position: absolute;
    left: 0;
    top: 0;
    width: 106px;
    height: 666px;
    background: var(--band-red);
  }
  .side-band-edge {
    position: absolute;
    left: 106px;
    top: 0;
    width: 22px;
    height: 666px;
    background: linear-gradient(90deg, var(--band-shadow), rgba(107, 52, 24, 0.35));
  }
  .logo-placeholder {
    position: absolute;
    left: 212px;
    top: 108px;
    margin: 0;
    font-size: 40px;
    font-weight: 400;
    line-height: 1;
    white-space: nowrap;
  }
  .logo-rule {
    position: absolute;
    left: 205px;
    top: 161px;
    width: 300px;
    height: 2px;
    background: var(--ink-light);
  }
  .contact {
    position: absolute;
    left: 449px;
    top: 347px;
    height: 260px;
    border-left: 9px solid var(--ink-light);
    padding-left: 18px;
  }
  .contact p {
    margin: 0;
    font-size: 40px;
    line-height: 52.5px;
    white-space: nowrap;
  }
  .contact .phone {
    font-weight: 700;
  }
  .corner-ornament {
    position: absolute;
    right: 0;
    bottom: 0;
    width: 190px;
    height: 130px;
    border-top-left-radius: 95px 80px;
    background: radial-gradient(ellipse at 70% 70%, var(--ornament-red) 0%, rgba(160, 74, 50, 0.6) 60%, rgba(160, 74, 50, 0) 100%);
  }
</style>
</head>
<body>
  <div class="card">
    <div class="side-band" role="img" aria-label="Decorative scroll pattern running down the left edge"></div>
    <div class="side-band-edge"></div>

    <p class="logo-placeholder">Company Logo</p>
    <div class="logo-rule"></div>

    <div class="contact">
      <p>Blue Fern café and function</p>
      <p>centre @ hallam orchard.</p>
      <p>wedding and function specialists,</p>
      <p>Barrow parkway, dunmore,</p>
      <p class="phone">ph 0438157240</p>
    </div>

    <div class="corner-ornament" role="img" aria-label="Decorative scroll ornament in the bottom right corner"></div>
  </div>
</body>
</html>
```